KRV Business Cards

We are a local commercial development company based in Silicon Valley and we would like a new business card. I've attached a copy of our company brochure to give a flavor of what we do, our logo, info company colors/graphics, and our current business card. We don't necessarily need a crazy makeover, but would like something that feels a little bit more "fresh" and modern (we've had the same business card design for 15+ years), but still in keeping with our overall brand -- clean, high-quality, modern but timeless. Would like to add our website to the info on the card (www.lumbrel.com) and would like the flexibility for some folks to have an efax number listed and some not to have that included (without it looking like there is a hole).

```html
<!DOCTYPE html>
<html lang="en">
<head>
<meta charset="utf-8">
<title>KRV Business Cards</title>
<link rel="stylesheet" href="https://fonts.googleapis.com/css2?family=Work+Sans:wght@400;500&display=swap">
<style>
  :root {
    --backdrop: #1e1f21;
    --card: #36536e;
    --ink: #ffffff;
    --ink-soft: #e6ecf2;
    --card-w: 640px;
    --card-h: 366px;
  }
  * { box-sizing: border-box; margin: 0; padding: 0; }
  html, body {
    width: 1200px; height: 900px; overflow: hidden;
    background: var(--backdrop);
  }
  .sheet {
    width: 1200px; height: 900px;
    display: flex; flex-direction: column; align-items: center; justify-content: center;
    gap: 44px;
  }
  .card {
    position: relative;
    width: var(--card-w); height: var(--card-h);
    background: var(--card);
    color: var(--ink);
  }
  .company-name {
    font-family: "Work Sans", Arial, sans-serif;
    font-weight: 400;
    line-height: 1.15;
    letter-spacing: 0.01em;
    color: var(--ink);
  }
  .card-front .company-name {
    position: absolute; left: 168px; top: 112px;
    font-size: 38px;
  }
  .card-back .company-name {
    position: absolute; left: 52px; top: 138px;
    font-size: 28px;
  }
  .divider {
    position: absolute; left: 346px; top: 82px;
    width: 2px; height: 204px; background: var(--ink);
  }
  .contact {
    position: absolute; left: 382px; top: 86px;
    font-family: "Work Sans", Arial, sans-serif;
    color: var(--ink-soft);
  }
  .contact-name {
    font-size: 23px; font-weight: 500; color: var(--ink); letter-spacing: 0.01em;
  }
  .contact-title {
    font-size: 14px; letter-spacing: 0.06em; margin: 2px 0 0 1px;
  }
  .contact-address {
    font-size: 15.5px; letter-spacing: 0.08em; line-height: 1.3; margin-top: 16px;
  }
  .contact-lines {
    list-style: none; margin-top: 14px;
    font-size: 15.5px; letter-spacing: 0.08em; line-height: 1.38;
  }
  .contact-lines li { display: flex; align-items: center; gap: 10px; }
  .contact-lines svg { width: 11px; height: 11px; flex: none; fill: var(--ink); }
</style>
</head>
<body>
<main class="sheet">
  <section class="card card-front" aria-label="Card front">
    <div class="company-name">Lumbrel<br>Realty Group</div>
  </section>

  <section class="card card-back" aria-label="Card back">
    <div class="company-name">Lumbrel<br>Realty Group</div>
    <div class="divider"></div>
    <div class="contact">
      <p class="contact-name">Dana J. Whitford</p>
      <p class="contact-title">Partner</p>
      <p class="contact-address">218 Harlow Street<br>Menlo Park, CA 94025</p>
      <ul class="contact-lines">
        <li>
          <svg viewBox="0 0 12 12" aria-hidden="true"><path d="M2.4 0.6 L4.2 0.4 L5 3 L3.8 4 Q4.8 6.6 7.8 8.2 L8.9 7 L11.5 7.8 L11.3 9.7 Q10.6 11.4 8.8 11.2 Q2.2 9.6 0.8 2.8 Q0.8 1 2.4 0.6 Z"/></svg>
          <span>650.555.0147</span>
        </li>
        <li>
          <svg viewBox="0 0 12 12" aria-hidden="true"><rect x="3" y="0.5" width="6" height="3.5"/><rect x="0.5" y="4.5" width="11" height="5" rx="1"/><rect x="3" y="8" width="6" height="3.5"/></svg>
          <span>650.555.0182</span>
        </li>
        <li>
          <svg viewBox="0 0 12 12" aria-hidden="true"><path d="M0.5 2 H11.5 V10 H0.5 Z M1.5 3 V9 H10.5 V3 L6 6.6 Z M2 3 L6 5.8 L10 3 Z" fill-rule="evenodd"/></svg>
          <span>info@lumbrel.com</span>
        </li>
        <li>
          <svg viewBox="0 0 12 12" aria-hidden="true"><path d="M6 0.5 A5.5 5.5 0 1 0 6 11.5 A5.5 5.5 0 1 0 6 0.5 Z M6 1.5 Q4.2 3.5 4.2 6 Q4.2 8.5 6 10.5 Q7.8 8.5 7.8 6 Q7.8 3.5 6 1.5 Z M1.5 5.5 H10.5 V6.5 H1.5 Z" fill-rule="evenodd"/></svg>
          <span>www.lumbrel.com</span>
        </li>
      </ul>
    </div>
  </section>
</main>
</body>
</html>
```